Business card

I need a business card design for my consulting company in animal welfare for livestock. I like clean, crisp, simple.

One I imagined was double-sided:
side1: just my name and contact information
side2: silhouette of farm animals. Could be 3 (pig, cow, chicken) or all the species (pig, cow, chicken, duck, sheep, rabbit, etc) that continue the length of the card. I have attached an image of a silhouette style.

But, I am open to any concept.

Industry/Entity Type

Business

```html
<!DOCTYPE html>
<html lang="en">
<head>
<meta charset="utf-8">
<title>Marion Halbrook – Business Card</title>
<link rel="stylesheet" href="https://fonts.googleapis.com/css2?family=Arimo:wght@400&display=swap">
<style>
  :root {
    --card-bg: #ffffff;
    --ink: #000000;
  }
  html, body {
    margin: 0;
    padding: 0;
    width: 1200px;
    height: 741px;
    overflow: hidden;
    background: var(--card-bg);
  }
  .card {
    position: relative;
    width: 1200px;
    height: 741px;
    background: var(--card-bg);
    color: var(--ink);
    font-family: "Arimo", Arial, sans-serif;
    font-weight: 400;
  }
  .card-line {
    position: absolute;
    left: 0;
    width: 100%;
    text-align: center;
    line-height: 54px;
    font-size: 53px;
    white-space: nowrap;
  }
  .tagline { top: 122px; }
  .owner-name { top: 316px; }
  .phone { top: 509px; }
  .email { top: 574px; }
</style>
</head>
<body>
  <main class="card">
    <p class="card-line tagline">Welfare Services for Livestock Stakeholders</p>
    <p class="card-line owner-name">Marion Halbrook</p>
    <p class="card-line phone">+1.604.555.0182</p>
    <p class="card-line email">marion.halbrook@mailbox.com</p>
  </main>
</body>
</html>
```